Tech Startup Needs Business Card Design

I am looking for an eye catching business card design for our new company, Torn Kite. We are a place for business owners and contractors to share their experiences with their customers and check their current customers. Our website, www.torn-kite.co, may be able to offer some guidance as to the design.

Industry/Entity Type

Business

Contact Information for Business Card

Owen Barthwick
888-417-3083
Owen@torn-kite.co
www.torn-kite.co

```html
<!DOCTYPE html>
<html lang="en">
<head>
<meta charset="utf-8">
<title>Torn Kite — Business Card</title>
<link rel="stylesheet" href="https://fonts.googleapis.com/css2?family=Roboto:wght@300;400;500;700&display=swap">
<style>
  :root {
    --brand-red: #ec1c24;
    --brand-green: #17a34a;
    --ink: #1b1b1b;
    --paper: #ffffff;
    --stage: #eceae6;
    --card-w: 660px;
    --card-h: 377px;
  }
  * { margin: 0; padding: 0; box-sizing: border-box; }
  html, body {
    width: 1200px;
    height: 950px;
    overflow: hidden;
    background: var(--stage);
    font-family: "Roboto", Arial, sans-serif;
  }
  .canvas {
    position: relative;
    width: 1200px;
    height: 950px;
  }
  .card {
    position: absolute;
    left: 270px;
    width: var(--card-w);
    height: var(--card-h);
    overflow: hidden;
    box-shadow: 0 10px 28px rgba(0,0,0,0.18);
  }

  /* Front side */
  .card-front {
    top: 70px;
    background: var(--brand-red);
  }
  .front-mark {
    position: absolute;
    left: 0;
    right: 0;
    top: 140px;
    display: flex;
    align-items: center;
    justify-content: center;
    gap: 14px;
  }
  .front-mark .dot {
    width: 34px;
    height: 34px;
    border-radius: 50%;
    background: var(--paper);
  }
  .front-mark .name {
    color: var(--paper);
    font-weight: 700;
    font-size: 46px;
    letter-spacing: 0.5px;
  }
  .front-web {
    position: absolute;
    left: 160px;
    top: 282px;
    color: var(--paper);
    font-size: 13px;
    font-weight: 400;
    letter-spacing: 3px;
  }

  /* Back side */
  .card-back {
    top: 500px;
    background: var(--paper);
  }
  .back-bands {
    position: absolute;
    inset: 0;
  }
  .back-mark {
    position: absolute;
    left: 160px;
    top: 52px;
    display: flex;
    align-items: center;
    gap: 14px;
  }
  .back-mark .dot {
    width: 30px;
    height: 30px;
    border-radius: 50%;
    background: var(--brand-red);
  }
  .back-mark .name {
    color: var(--ink);
    font-weight: 700;
    font-size: 58px;
    letter-spacing: 0.5px;
  }
  .person {
    position: absolute;
    right: 446px;
    top: 280px;
    text-align: right;
    color: var(--paper);
  }
  .person .full-name {
    font-weight: 700;
    font-size: 19px;
  }
  .person .role {
    font-weight: 300;
    font-size: 15px;
    margin-top: 3px;
  }
  .divider {
    position: absolute;
    left: 230px;
    top: 268px;
    width: 1px;
    height: 70px;
    background: rgba(255,255,255,0.75);
  }
  .contacts {
    position: absolute;
    left: 246px;
    top: 268px;
    list-style: none;
    color: var(--paper);
    font-size: 15px;
    font-weight: 400;
  }
  .contacts li {
    display: flex;
    align-items: center;
    gap: 8px;
    height: 23px;
  }
  .contacts svg {
    width: 14px;
    height: 14px;
    flex: none;
  }
</style>
</head>
<body>
<main class="canvas">

  <section class="card card-front" aria-label="Card front">
    <div class="front-mark">
      <span class="dot"></span>
      <span class="name">Torn Kite</span>
    </div>
    <p class="front-web">www.torn-kite.co</p>
  </section>

  <section class="card card-back" aria-label="Card back">
    <svg class="back-bands" viewBox="0 0 660 377" preserveAspectRatio="none" aria-hidden="true">
      <path d="M0,110 Q300,250 660,262 L660,377 L0,377 Z" fill="var(--brand-green)"/>
      <path d="M0,118 Q300,264 660,280 L660,377 L0,377 Z" fill="var(--brand-red)"/>
    </svg>

    <div class="back-mark">
      <span class="dot"></span>
      <span class="name">Torn Kite</span>
    </div>

    <div class="person">
      <p class="full-name">Owen Barthwick</p>
      <p class="role">President</p>
    </div>

    <span class="divider"></span>

    <ul class="contacts">
      <li>
        <svg viewBox="0 0 16 16" aria-hidden="true"><path fill="#fff" d="M3.6 1.5l2.3 2.6-1.3 1.6c.9 2 2.6 3.7 4.6 4.6l1.6-1.3 2.6 2.3-1.3 2.2C7 13.4 2.6 9 2.4 2.8z"/></svg>
        <span>888-417-3083</span>
      </li>
      <li>
        <svg viewBox="0 0 16 16" aria-hidden="true"><rect x="1" y="3" width="14" height="10" rx="1" fill="#fff"/><path d="M1.5 3.8L8 9l6.5-5.2" fill="none" stroke="var(--brand-red)" stroke-width="1.3"/></svg>
        <span>Owen@torn-kite.co</span>
      </li>
      <li>
        <svg viewBox="0 0 16 16" aria-hidden="true"><circle cx="8" cy="8" r="7" fill="#fff"/><g fill="none" stroke="var(--brand-red)" stroke-width="1"><ellipse cx="8" cy="8" rx="3" ry="6"/><path d="M2 8h12M3 5h10M3 11h10"/></g></svg>
        <span>www.torn-kite.co</span>
      </li>
    </ul>
  </section>

</main>
</body>
</html>
```